FOOD DELIVERY BRAND NEEDS WEBSITE TO GET SUBSCRIBERS

web design needed for a food delivery brand/label,
website should display who we are, how it works and push futur clients to get the label for an online application. Should look serious/official, trustworthy and confident. colors are black and gold like logo

Target Market(s)

restaurants

Industry/Entity Type

restaurant

Number of Pages Required

4 page

Requirements
Must have
• home page, who we are, our partners, subscribe, 2 subscribe button : 1 on top 1 bottom
Nice to have
• a graphic showing average + 15% sales thanks the label

```html
<!DOCTYPE html>
<html lang="en">
<head>
<meta charset="utf-8">
<title>Amber Spoon Seal — Subscribe</title>
<link href="https://fonts.googleapis.com/css2?family=Poppins:wght@400;500;600;700&family=Lato:wght@400;700&display=swap" rel="stylesheet">
<style>
:root{
  --gold:#e6b000;
  --gold-deep:#d09c00;
  --ink:#111111;
  --header:#e9e9e9;
  --nav-text:#1c1c1c;
  --modal-bg:#eef7f1;
  --heading:#3a3a3a;
  --body:#4a4a4a;
  --white:#ffffff;
  --dim:rgba(0,0,0,.78);
}
*{margin:0;padding:0;box-sizing:border-box}
html,body{width:1200px;height:638px;overflow:hidden}
body{position:relative;font-family:"Poppins",sans-serif;background:#1a140d}

.page{position:absolute;inset:0}
.hero-photo{position:absolute;left:0;top:75px;width:1200px;height:563px;
  background:radial-gradient(ellipse at 30% 30%,#6b5436 0%,#3e2e1c 45%,#22180f 100%)}
.site-header{position:absolute;left:0;top:0;width:1200px;height:75px;background:var(--header)}
.brand{position:absolute;left:112px;top:0;width:150px;height:148px;background:var(--ink);
  display:flex;align-items:center;justify-content:center;gap:6px}
.brand-dot{width:10px;height:10px;border-radius:50%;background:var(--gold)}
.brand-name{font-family:"Poppins",sans-serif;font-weight:600;font-size:11px;color:var(--gold);letter-spacing:.5px}
.main-nav{position:absolute;left:285px;top:27px;display:flex;font-weight:600;font-size:15px;color:var(--nav-text)}
.main-nav a{color:inherit;text-decoration:none;padding:0 29px;border-right:1px solid #c9c9c9;line-height:22px}
.main-nav a:last-child{border-right:none}
.main-nav a:first-child{padding-left:23px}
.btn-top{position:absolute;left:953px;top:19px;width:135px;height:40px;background:var(--gold);
  color:var(--white);font-weight:600;font-size:11px;display:flex;align-items:center;justify-content:center;border-radius:2px}

.search-bar{position:absolute;left:187px;top:303px;width:826px;height:75px;border:1px solid rgba(255,255,255,.5)}
.search-input{position:absolute;left:15px;top:16px;width:300px;height:43px;background:var(--white);
  font-family:"Lato",sans-serif;font-size:9px;color:#888;display:flex;align-items:center;padding-left:20px;gap:5px}
.search-btn{position:absolute;left:679px;top:16px;width:132px;height:43px;background:var(--gold);color:var(--white);
  font-weight:600;font-size:11px;display:flex;align-items:center;justify-content:center}

.stat{position:absolute;top:420px;display:flex;align-items:center;gap:12px}
.stat-icon{width:68px;height:68px;border-radius:50%;background:#ffffff}
.stat-num{font-weight:700;font-size:26px;color:var(--white);line-height:1}
.stat-label{font-family:"Lato",sans-serif;font-size:12px;color:var(--white);margin-top:6px}

.mascot-art{position:absolute;left:33px;top:492px;width:125px;height:146px;
  background:linear-gradient(180deg,#f2c400 0%,#f5f0e6 70%);border-radius:60px 60px 0 0}
.cloud-art{position:absolute;left:833px;top:529px;width:367px;height:109px;
  background:linear-gradient(180deg,#ffffff,#f0f0f0);border-radius:140px 140px 0 0}

.dim{position:absolute;inset:0;background:var(--dim)}

.modal{position:absolute;left:329px;top:164px;width:542px;height:310px;background:var(--modal-bg);overflow:hidden}
.modal-art{position:absolute;right:0;top:0;width:188px;height:310px;
  background:linear-gradient(160deg,rgba(238,247,241,0) 0%,#e9d9c4 40%,#f3d34a 65%,#b7d9a6 100%)}
.close{position:absolute;left:503px;top:17px;width:22px;height:22px;border-radius:50%;background:#2b2b2b;
  display:flex;align-items:center;justify-content:center}
.envelope{position:absolute;left:42px;top:42px}
.modal-title{position:absolute;left:92px;top:43px;width:250px;font-weight:500;font-size:18.5px;line-height:17px;color:var(--heading);text-transform:uppercase}
.modal-text{position:absolute;left:42px;top:106px;width:320px;font-family:"Lato",sans-serif;font-size:12.8px;line-height:20.8px;color:var(--body)}
.email-form{position:absolute;left:42px;top:183px;width:391px;height:46px;background:var(--white);border-radius:23px;
  box-shadow:0 3px 10px rgba(0,0,0,.08)}
.email-field{position:absolute;left:25px;top:0;height:46px;display:flex;align-items:center;font-size:8.5px;color:#555;text-transform:uppercase}
.btn-subscribe{position:absolute;left:277px;top:4px;width:110px;height:38px;border-radius:19px;background:var(--gold-deep);
  color:var(--white);font-weight:600;font-size:11.5px;display:flex;align-items:center;justify-content:center;text-transform:uppercase}
.notice{position:absolute;left:42px;top:254px;display:flex;align-items:center;gap:9px;font-size:12.3px;color:var(--gold-deep)}
</style>
</head>
<body>
<div class="page">
  <div class="hero-photo" role="img" aria-label="Dark overhead photo of plated dishes on a wooden table"></div>
  <header class="site-header">
    <div class="brand"><span class="brand-dot"></span><span class="brand-name">AMBER SPOON SEAL</span></div>
    <nav class="main-nav"><a>About Us</a><a>How it Works</a><a>Our Partners</a><a>Login / Signup</a></nav>
    <div class="btn-top">SUBSCRIBE</div>
  </header>

  <div class="search-bar">
    <div class="search-input">
      <svg width="7" height="9" viewBox="0 0 7 9"><path d="M3.5 0a3 3 0 0 0-3 3c0 2.2 3 6 3 6s3-3.8 3-6a3 3 0 0 0-3-3z" fill="#888"/></svg>
      Search Location
    </div>
    <div class="search-btn">SEARCH</div>
  </div>

  <div class="stat" style="left:198px"><div class="stat-icon"></div><div><div class="stat-num">1000+</div><div class="stat-label">Restaurants</div></div></div>
  <div class="stat" style="left:405px"><div class="stat-icon"></div><div><div class="stat-num">2000+</div><div class="stat-label">People served</div></div></div>
  <div class="stat" style="left:612px"><div class="stat-icon"></div><div><div class="stat-num">800+</div><div class="stat-label">Happy clients</div></div></div>
  <div class="stat" style="left:820px"><div class="stat-icon"></div><div><div class="stat-num">500+</div><div class="stat-label">Regular users</div></div></div>

  <div class="mascot-art" role="img" aria-label="Cartoon delivery rider illustration"></div>
  <div class="cloud-art" role="img" aria-label="Decorative cloud illustration"></div>
</div>

<div class="dim"></div>

<section class="modal" aria-label="Newsletter signup">
  <div class="modal-art" role="img" aria-label="Photo of bananas, beans and fresh greens"></div>
  <div class="close">
    <svg width="8" height="8" viewBox="0 0 8 8"><path d="M1 1l6 6M7 1L1 7" stroke="#fff" stroke-width="1.8" stroke-linecap="round"/></svg>
  </div>
  <svg class="envelope" width="34" height="33" viewBox="0 0 34 33">
    <path d="M17 0L34 12V33H0V12Z" fill="#d09c00"/>
    <path d="M6 16l11 8 11-8" stroke="#fff" stroke-width="2.2" fill="none" stroke-linecap="round" stroke-linejoin="round"/>
  </svg>
  <h2 class="modal-title">Sign up for recent updates</h2>
  <p class="modal-text">Join our Subscribers list to get the latest news, updates and special offers delivered directly in your inbox.</p>
  <div class="email-form">
    <div class="email-field">Enter your email</div>
    <div class="btn-subscribe">Subscribe</div>
  </div>
  <div class="notice">
    <svg width="11" height="9" viewBox="0 0 11 9"><path d="M1 4.5l3 3L10 1" stroke="#d09c00" stroke-width="2" fill="none" stroke-linecap="round" stroke-linejoin="round"/></svg>
    Thanks, your address has been added.
  </div>
</section>
</body>
</html>
```